Modern Label for cleaning products for the brand Voralux

We need a label design for our line of cleaning products. The label should feature our logo and an image to identify the product's intended use. I've added our logo and an image for use. This only concerns the design of the label on the front of the bottle.

Label dimensions:
Label 1 (500ml bottle with spray): width 58mm x height 115mm
Label 2: (1L bottle): width 73mm x height 140mm
The design must be consistent for both bottles which you find in the pictures.

The bottles to be labeled are white. See the attachment for a photo of the bottles.

The photo must also appear on the label to identify the product's intended use.

Product information:
Brand: Voralux
Product: Sanitary Cleaner

This text must be placed on the label:
"Cleans, descales & freshens. followed with this text: "Ideal for quick and powerful cleaning. A ready-to-use product for everyday use."

- Mention the seperate USP's: Sanitary, Bathroom, Toilet, Wet areas

Appearance: This is a consumer product, but it must have a professional appearance. We would like to see a design that use the color blue from our logo.

Target Market(s)

Consumers who take care of their homes and want to maintain it the correct (professional) way

Font styles to use
Sans Serif

Colors
0054AA
0677BA
7BADD7
CADEEF
E8F1F8

Requirements
Must have
• USP's + use of image and logo + blend in 1 design
Nice to have
• Keep the color of the logo in the design
Should not have
• Comic sans

```html
<!DOCTYPE html>
<html lang="en">
<head>
<meta charset="utf-8">
<title>Voralux Sanitary Cleaner – Label Set</title>
<link rel="stylesheet" href="https://fonts.googleapis.com/css2?family=Oswald:wght@500&family=Poppins:wght@400;600&display=swap">
<style>
  :root {
    --backdrop: #efebe6;
    --brand-deep: #0054aa;
    --brand-blue: #0677ba;
    --brand-mid: #2a8ccb;
    --brand-light: #7badd7;
    --brand-pale: #cadeef;
    --brand-mist: #e8f1f8;
    --accent-lime: #c8d44a;
    --white: #ffffff;
    --photo-wall: #d9d6d2;
    --photo-tile: #f3f3f1;
    --photo-floor: #a8a39c;
  }
  html, body {
    margin: 0;
    width: 1200px;
    height: 1200px;
    overflow: hidden;
    background: var(--backdrop);
  }
  .label-set {
    position: relative;
    width: 1200px;
    height: 1200px;
  }
  .label {
    position: absolute;
    display: block;
    box-shadow: 0 6px 24px rgba(0, 0, 0, 0.12);
  }
  .label--500ml { left: 101px; top: 285px; width: 406px; height: 805px; }
  .label--1l    { left: 587px; top: 110px; width: 511px; height: 980px; }

  .brand-name { font-family: "Poppins", sans-serif; font-weight: 600; fill: var(--white); }
  .headline   { font-family: "Oswald", sans-serif; font-weight: 500; fill: var(--white); letter-spacing: 1px; }
  .body-copy  { font-family: "Poppins", sans-serif; font-weight: 400; fill: var(--white); }
  .usp-label  { font-family: "Poppins", sans-serif; font-weight: 400; fill: var(--white); }
  .usp-ring   { fill: none; stroke: var(--white); stroke-width: 2; }
  .logo-ring  { fill: none; stroke: var(--white); }
  .divider    { stroke: var(--white); stroke-width: 1.5; }
  .divider-accent { stroke: var(--accent-lime); stroke-width: 1.5; }
</style>
</head>
<body>
<main class="label-set">

  <!-- 500 ml spray bottle label, 58 x 115 mm -->
  <svg class="label label--500ml" viewBox="0 0 580 1150" xmlns="http://www.w3.org/2000/svg">
    <defs>
      <linearGradient id="photo-tones-a" x1="0" y1="0" x2="1" y2="1">
        <stop offset="0" stop-color="#b9b3ad"/>
        <stop offset="0.45" stop-color="#e9e8e5"/>
        <stop offset="0.75" stop-color="#f4f4f2"/>
        <stop offset="1" stop-color="#a8a39c"/>
      </linearGradient>
      <linearGradient id="blob-a" x1="0" y1="0" x2="0" y2="1">
        <stop offset="0" stop-color="#0a6fbd"/>
        <stop offset="1" stop-color="#1a84c6"/>
      </linearGradient>
    </defs>
    <rect class="label-photo" width="580" height="1150" fill="url(#photo-tones-a)" role="img" aria-label="Photo of a bright modern bathroom with a washbasin, mirror, white wall tiles and a bathtub with mosaic front"/>
    <path class="label-wave" fill="url(#blob-a)"
      d="M0 600 C 30 470 110 420 190 430 C 280 440 330 560 380 680 C 410 760 440 800 470 800 L 580 800 L 580 1150 L 0 1150 Z"/>
    <circle class="label-bump" cx="560" cy="700" r="145" fill="var(--brand-mid)"/>
    <circle cx="188" cy="640" r="56" class="logo-ring" stroke-width="11"/>
    <text class="brand-name" x="188" y="742" font-size="50" text-anchor="middle">voralux</text>
    <line class="divider" x1="48" y1="812" x2="300" y2="812"/>
    <line class="divider-accent" x1="300" y1="812" x2="350" y2="812"/>
    <text class="headline" x="48" y="850" font-size="25">CLEANS, DESCALES &amp; FRESHENS</text>
    <text class="body-copy" x="48" y="878" font-size="15.5">Ideal for Quick and Powerful Cleaning.</text>
    <text class="body-copy" x="48" y="898" font-size="15.5">A Ready-To-Use Product for Everyday Use</text>
    <g class="usp-row">
      <circle class="usp-ring" cx="80" cy="975" r="32"/>
      <text class="usp-label" x="80" y="998" font-size="8" text-anchor="middle">Sanitary</text>
      <circle class="usp-ring" cx="170" cy="975" r="32"/>
      <text class="usp-label" x="170" y="998" font-size="8" text-anchor="middle">Bathroom</text>
      <circle class="usp-ring" cx="259" cy="975" r="32"/>
      <text class="usp-label" x="259" y="998" font-size="8" text-anchor="middle">Toilet</text>
      <circle class="usp-ring" cx="348" cy="975" r="32"/>
      <text class="usp-label" x="348" y="998" font-size="8" text-anchor="middle">Wet areas</text>
    </g>
    <circle class="dot-accent" cx="107" cy="1062" r="42" fill="var(--brand-mid)"/>
    <ellipse class="base-arc" cx="395" cy="1152" rx="115" ry="90" fill="var(--white)"/>
  </svg>

  <!-- 1 L bottle label, 73 x 140 mm -->
  <svg class="label label--1l" viewBox="0 0 730 1400" xmlns="http://www.w3.org/2000/svg">
    <defs>
      <linearGradient id="photo-tones-b" x1="0" y1="0" x2="1" y2="1">
        <stop offset="0" stop-color="#b9b3ad"/>
        <stop offset="0.45" stop-color="#e9e8e5"/>
        <stop offset="0.75" stop-color="#f4f4f2"/>
        <stop offset="1" stop-color="#a8a39c"/>
      </linearGradient>
      <linearGradient id="blob-b" x1="0" y1="0" x2="0" y2="1">
        <stop offset="0" stop-color="#0a6fbd"/>
        <stop offset="1" stop-color="#1a84c6"/>
      </linearGradient>
    </defs>
    <rect class="label-photo" width="730" height="1400" fill="url(#photo-tones-b)" role="img" aria-label="Photo of a bright modern bathroom with a washbasin, mirror, white wall tiles and a bathtub with mosaic front"/>
    <path class="label-wave" fill="url(#blob-b)"
      d="M0 820 C 20 640 80 530 170 524 C 280 518 350 680 420 840 C 460 930 490 1000 530 1010 L 730 1010 L 730 1400 L 0 1400 Z"/>
    <circle class="label-bump" cx="700" cy="950" r="180" fill="var(--brand-mid)"/>
    <circle cx="246" cy="785" r="66" class="logo-ring" stroke-width="13"/>
    <text class="brand-name" x="246" y="912" font-size="66" text-anchor="middle">voralux</text>
    <line class="divider" x1="74" y1="993" x2="390" y2="993"/>
    <line class="divider-accent" x1="390" y1="993" x2="443" y2="993"/>
    <text class="headline" x="74" y="1037" font-size="30">CLEANS, DESCALES &amp; FRESHENS</text>
    <text class="body-copy" x="74" y="1068" font-size="19">Ideal for Quick and Powerful Cleaning.</text>
    <text class="body-copy" x="74" y="1093" font-size="19">A Ready-To-Use Product for Everyday Use</text>
    <g class="usp-row">
      <circle class="usp-ring" cx="113" cy="1196" r="39"/>
      <text class="usp-label" x="113" y="1224" font-size="9.5" text-anchor="middle">Sanitary</text>
      <circle class="usp-ring" cx="222" cy="1196" r="39"/>
      <text class="usp-label" x="222" y="1224" font-size="9.5" text-anchor="middle">Bathroom</text>
      <circle class="usp-ring" cx="331" cy="1196" r="39"/>
      <text class="usp-label" x="331" y="1224" font-size="9.5" text-anchor="middle">Toilet</text>
      <circle class="usp-ring" cx="438" cy="1196" r="39"/>
      <text class="usp-label" x="438" y="1224" font-size="9.5" text-anchor="middle">Wet areas</text>
    </g>
    <circle class="dot-accent" cx="143" cy="1317" r="53" fill="var(--brand-mid)"/>
    <ellipse class="base-arc" cx="494" cy="1402" rx="136" ry="115" fill="var(--white)"/>
  </svg>

</main>
</body>
</html>
```